依頼詳細
街でよく見かけるのぼり旗より“ちょっといいデザイン”のひな形を求めています。弊社が求めているデザインの割合は以下3点です。

1. 10年後も古くならないもの(6割)
2. おしゃれなもの(3割)
3. ふりきってるもの(1割)

今回の依頼は2.または3.を意識して制作をお願いいたします。
他ののぼり屋さんでよく見かけるような「大きな袋文字でドカーン」といったデザインは求めていません。
今回は「高級なデザイン」というよりも「親しみやすい」デザインを求めています。
記載項目
【注意点】

1.「入居者募集」という文字でデザインを制作してください。

2. イラスト、写真の有無は自由。英語表記を追加するのも自由です。

3.写真などをご使用いただいても結構ですが権利などを侵害しないことを確認してください。
※イメージ写真を使う場合はその旨をお伝えください。
(デザイン決定後に当店で似たイメージ写真を探し、差し替えいたします)

デザインのぼりショップHP
https://www.kumoiro-hata.com

【制作上の注意点】
◎文字変更がカンタンなデータ(採用デザインをベースに文字変更や色変更を弊社で行う場合があります)
◎仕様:2種類(左チチ/袋縫い)に対応できるデザイン
◎複雑なフィルターを使って重いデータにならないこと
◎拡大縮小によるミスが起こりにくいデータが望ましい(入稿データ作成時はスウォッチを分割するなど)

※詳細は添付ファイル「のぼり旗デザイン制作_外部委託資料.pdf」をご確認お願いいたします。
※ラフデザイン制作用に「AAA001_018.pdf」をイラストレーターで開いて使用ください。
希望イメージ
シンプル 複雑
単色 カラフル
暗い 明るい
日常 高級
遊び心 厳粛
未来的 伝統的
女性的 男性的
希望する色
納品ファイル
• イラストレーター形式 (.ai)
補足説明
数々のご提案ありがとうございます。
9月20日が締め切りで週明けの24日以降なるべく早く決定したいと思います。
どうぞよろしくお願いします。
■ 選んだ理由

文字の視認性、展開のしやすさ、他ののぼり屋さんにないデザインという観点で選定させていただきました。

■ 提案者全員のお礼・コメント

他にも何点か迷うデザインがありましたが、今回は見送らせていただきました。ご応募いただいた皆様、大変にありがとうございました。また機会がありましたら、よろしくお願いします。

```html
<!DOCTYPE html>
<html lang="ja">
<head>
<meta charset="utf-8">
<title>入居者募集 のぼり旗</title>
<link rel="stylesheet" href="https://fonts.googleapis.com/css2?family=Noto+Sans+JP:wght@700;900&family=Oswald:wght@600&family=Great+Vibes&display=swap">
<style>
  :root{
    --bg:#ededed;
    --tab:#ffffff;
    --tab-line:#b9b9b9;
    --sale-top:#f5a020;
    --sale-bottom:#fde6b8;
    --sale-cell:#fbc97a;
    --sale-char:#c8161d;
    --rent-top:#3a78c6;
    --rent-bottom:#d3e3f2;
    --rent-cell:#7fb0e2;
    --rent-char:#ffe100;
    --rent-char-line:#1d4f93;
    --white:#ffffff;
    --confetti-a:rgba(255,60,90,.28);
    --confetti-b:rgba(60,200,110,.26);
    --confetti-c:rgba(255,230,40,.3);
    --confetti-d:rgba(60,140,255,.26);
  }
  *{margin:0;padding:0;box-sizing:border-box}
  html,body{width:846px;height:1200px;overflow:hidden;background:var(--bg)}
  .stage{position:relative;width:846px;height:1200px}
  .flag{position:absolute;top:113px;width:288px;height:1002px}
  .flag--sale{left:113px}
  .flag--rent{left:437px}
  .flag__cloth{position:absolute;inset:0;overflow:hidden}
  .flag--sale .flag__cloth{background:linear-gradient(180deg,var(--sale-top) 0%,var(--sale-top) 15%,var(--sale-bottom) 100%)}
  .flag--rent .flag__cloth{background:linear-gradient(180deg,var(--rent-top) 0%,var(--rent-top) 15%,var(--rent-bottom) 100%)}
  .flag__frame{position:absolute;left:12px;right:12px;top:22px;bottom:22px;border:2px solid var(--white);border-radius:4px}
  .flag__confetti{position:absolute;left:22px;right:22px;top:150px;bottom:70px;border-radius:20px;
    background:
      radial-gradient(circle at 15% 20%,var(--confetti-a) 0,transparent 22%),
      radial-gradient(circle at 85% 35%,var(--confetti-b) 0,transparent 22%),
      radial-gradient(circle at 20% 60%,var(--confetti-c) 0,transparent 24%),
      radial-gradient(circle at 80% 75%,var(--confetti-d) 0,transparent 22%),
      radial-gradient(circle at 30% 92%,var(--confetti-a) 0,transparent 20%),
      radial-gradient(circle at 75% 95%,var(--confetti-c) 0,transparent 20%)}
  .flag__ornament{position:absolute;left:50%;transform:translateX(-50%);background:rgba(255,255,255,.75)}
  .flag__ornament--top{top:14px;width:40px;height:14px;border-radius:7px}
  .flag__ornament--bottom{bottom:34px;width:70px;height:22px;border-radius:11px}
  .flag__for{position:absolute;top:30px;left:0;right:0;text-align:center;color:var(--white);
    font-family:"Great Vibes",cursive;font-size:30px;line-height:1}
  .flag__label{position:absolute;top:58px;left:0;right:0;text-align:center;color:var(--white);
    font-family:"Oswald",sans-serif;font-weight:600;font-size:44px;letter-spacing:2px;line-height:1}
  .flag__title{position:absolute;top:135px;left:65px;width:158px;display:flex;flex-direction:column;gap:6px}
  .flag__char{height:133px;border:4px solid var(--white);display:flex;align-items:center;justify-content:center;
    font-family:"Noto Sans JP",sans-serif;font-weight:900;font-size:112px;line-height:1}
  .flag--sale .flag__char{background:var(--sale-cell);color:var(--sale-char)}
  .flag--rent .flag__char{background:var(--rent-cell);color:var(--rent-char);
    -webkit-text-stroke:3px var(--rent-char-line);paint-order:stroke fill}
  .flag__note{position:absolute;right:18px;bottom:8px;color:var(--white);opacity:.8;
    font-family:"Noto Sans JP",sans-serif;font-weight:700;font-size:8px}
  .flag__ties{position:absolute;left:-26px;top:-16px;overflow:visible}
</style>
</head>
<body>
<main class="stage">

  <section class="flag flag--sale" aria-label="For SALE 入居者募集">
    <svg class="flag__ties" width="340" height="1040" aria-hidden="true">
      <g fill="var(--tab)" stroke="var(--tab-line)" stroke-width="1.5">
        <rect x="40" y="2" width="16" height="22"/><rect x="130" y="2" width="16" height="22"/><rect x="226" y="2" width="16" height="22"/>
        <rect x="2" y="18" width="30" height="14"/><rect x="2" y="175" width="30" height="14"/><rect x="2" y="335" width="30" height="14"/>
        <rect x="2" y="495" width="30" height="14"/><rect x="2" y="655" width="30" height="14"/><rect x="2" y="815" width="30" height="14"/>
      </g>
    </svg>
    <div class="flag__cloth">
      <div class="flag__confetti" role="img" aria-label="色とりどりの紙吹雪の散らし模様"></div>
      <div class="flag__frame"></div>
      <div class="flag__ornament flag__ornament--top" role="img" aria-label="枠上部の飾り模様"></div>
      <div class="flag__ornament flag__ornament--bottom" role="img" aria-label="枠下部の飾り模様"></div>
      <p class="flag__for">For</p>
      <p class="flag__label">SALE</p>
      <h1 class="flag__title">
        <span class="flag__char">入</span><span class="flag__char">居</span><span class="flag__char">者</span><span class="flag__char">募</span><span class="flag__char">集</span>
      </h1>
      <p class="flag__note">品番 A-01</p>
    </div>
  </section>

  <section class="flag flag--rent" aria-label="For RENT 入居者募集">
    <svg class="flag__ties" width="340" height="1040" aria-hidden="true">
      <g fill="var(--tab)" stroke="var(--tab-line)" stroke-width="1.5">
        <rect x="40" y="2" width="16" height="22"/><rect x="130" y="2" width="16" height="22"/><rect x="226" y="2" width="16" height="22"/>
        <rect x="2" y="18" width="30" height="14"/><rect x="2" y="175" width="30" height="14"/><rect x="2" y="335" width="30" height="14"/>
        <rect x="2" y="495" width="30" height="14"/><rect x="2" y="655" width="30" height="14"/><rect x="2" y="815" width="30" height="14"/>
      </g>
    </svg>
    <div class="flag__cloth">
      <div class="flag__confetti" role="img" aria-label="色とりどりの紙吹雪の散らし模様"></div>
      <div class="flag__frame"></div>
      <div class="flag__ornament flag__ornament--top" role="img" aria-label="枠上部の飾り模様"></div>
      <div class="flag__ornament flag__ornament--bottom" role="img" aria-label="枠下部の飾り模様"></div>
      <p class="flag__for">For</p>
      <p class="flag__label">RENT</p>
      <h2 class="flag__title">
        <span class="flag__char">入</span><span class="flag__char">居</span><span class="flag__char">者</span><span class="flag__char">募</span><span class="flag__char">集</span>
      </h2>
      <p class="flag__note">品番 A-02</p>
    </div>
  </section>

</main>
</body>
</html>
```